Hospitality project presentation

I am developing a hospitality project and I need to present to the developer an outstanding presentation highlighting the overall look and feel. I will provide the text and most of the pictures (not all of them) some pictures (copyright free) will hae to be provided by the designer. Maximum number of pages 15, and zoom calls with me to make some adjustment if needed.

Industry/Entity Type

Hospitality

Font styles to use
Other font styles liked:
• calibri light

Requirements
Must have
• 15 slides
Nice to have
• Hospitality resort project look and feel

```html
<!DOCTYPE html>
<html lang="en">
<head>
<meta charset="utf-8">
<title>Hospitality Project Brochure</title>
<link rel="stylesheet" href="https://fonts.googleapis.com/css2?family=Tinos:wght@400;700&display=swap">
<style>
:root{
  --navy:#1d3149;
  --navy-deep:#172a3f;
  --grey-bar:#8e8e90;
  --paper:#ffffff;
  --canvas:#e8e8e9;
  --sheet:#ffffff;
  --ink:#2b2b2b;
  --accent:#3b7bd1;
}
*{box-sizing:border-box;margin:0;padding:0}
html,body{width:1200px;height:4000px;overflow:hidden}
body{background:var(--canvas);font-family:"Tinos","Times New Roman",serif;color:var(--ink);position:relative}

.overview-sheet{position:absolute;left:0;top:2170px;width:1200px;height:1830px;background:var(--sheet)}

.spread{position:absolute;left:120px;width:960px;height:615px;display:flex;box-shadow:0 10px 30px rgba(0,0,0,.18)}
.spread::after{content:"";position:absolute;left:470px;top:0;width:20px;height:100%;background:linear-gradient(90deg,transparent,rgba(0,0,0,.12),transparent);pointer-events:none}
.spread--covers{top:80px}
.spread--intro{top:775px}
.spread--resort{top:1470px}

.grid{position:absolute;left:140px;top:2245px;width:920px;display:grid;grid-template-columns:400px 400px;column-gap:120px;row-gap:80px}
.grid .page{box-shadow:0 6px 18px rgba(0,0,0,.16)}

.page{position:relative;overflow:hidden;background:var(--paper)}
.page--lg{width:480px;height:615px;font-size:10px}
.page--sm{width:400px;height:512px;font-size:8.33px}

.photo{position:absolute}
.photo--pool{background:linear-gradient(180deg,#b8d2ec 0%,#d7e5f1 38%,#c9ccc7 52%,#6f95b8 62%,#2f63a8 100%)}
.photo--cafe{background:linear-gradient(180deg,#4a4744 0%,#7d746b 40%,#b3aba2 70%,#3c3a38 100%)}
.photo--dining{background:linear-gradient(135deg,#6b4a2f 0%,#a9774c 35%,#4f6a63 65%,#a9c7dc 100%)}
.photo--terrace{background:linear-gradient(180deg,#a7c4e4 0%,#cfdbe5 35%,#c98a72 48%,#e2dcd3 62%,#2f63a8 100%)}
.photo--lagoon{background:linear-gradient(180deg,#b7cfe6 0%,#dfe6ea 40%,#8e9c86 50%,#5f89b6 62%,#1f5aa6 100%)}
.photo--faint{background:linear-gradient(180deg,#23374e 0%,#1f3249 50%,#1b2d43 100%)}

.brand{font-family:"Tinos","Times New Roman",serif;font-weight:400;letter-spacing:.04em}

/* cover */
.cover__bar-left{position:absolute;left:0;top:0;width:6%;height:70%;background:var(--grey-bar)}
.cover__bar-right{position:absolute;right:0;top:70%;width:4%;height:30%;background:var(--grey-bar)}
.cover .photo{left:6%;right:4%;top:0;height:70%}
.cover__brand{position:absolute;left:6%;right:4%;top:12%;text-align:center;font-size:2.2em;color:var(--ink)}
.cover__band{position:absolute;left:6%;right:4%;top:70%;height:22%;background:var(--navy);display:flex;align-items:center;justify-content:center}
.cover__title{color:#fff;font-weight:700;font-size:3.5em;line-height:1.05;text-align:center;letter-spacing:.05em}
.cover__url{position:absolute;left:6%;right:4%;top:92%;height:8%;display:flex;align-items:center;justify-content:center;font-size:1.4em;letter-spacing:.14em}

/* back */
.back{background:var(--navy)}
.back .photo{left:3%;right:3%;top:2.5%;bottom:2.5%;opacity:.9}
.back__brand{position:absolute;left:0;right:0;top:78%;text-align:center;color:#fff;font-size:2.2em}
.back__contacts{position:absolute;left:6%;right:3%;top:90%;display:flex;justify-content:space-between;color:#fff;font-size:1.05em}
.contact{display:flex;flex-direction:column;align-items:center;gap:.4em}
.contact svg{width:1.2em;height:1.2em;fill:var(--accent)}
.contact__sep{align-self:flex-end;color:#fff}

/* shared text */
.heading{font-weight:700;font-size:1.55em;letter-spacing:.02em}
.body-copy{font-size:.78em;line-height:1.35;text-align:justify}
.body-copy + .body-copy{margin-top:1em}
.folio{position:absolute;left:11%;right:8%;bottom:3.5%;display:flex;justify-content:space-between;align-items:flex-end;font-size:.65em;border-bottom:1px solid currentColor;padding-bottom:.3em}
.folio__no{font-weight:700}

/* page 01 */
.p01 .photo{left:0;right:0;top:0;height:58%}
.p01__title{position:absolute;left:0;top:63%;display:flex;align-items:center;gap:.5em;font-size:2.4em;font-weight:400;color:var(--navy)}
.p01__mark{display:block;width:1.6em;height:.8em;background:var(--navy)}
.p01__text{position:absolute;left:11%;right:8%;top:72%}
.p01__text .body-copy{font-size:.72em}

/* page 02 */
.p02__panel{position:absolute;left:0;top:0;width:47%;height:100%;background:var(--navy)}
.p02 .photo{left:10%;right:7%;top:6%;height:33%}
.p02__left{position:absolute;left:10%;width:33%;top:43%;color:#fff}
.p02__left .heading{font-size:1.7em;margin-bottom:.2em}
.p02__left .body-copy{font-size:.74em;margin-bottom:1.2em}
.p02__right{position:absolute;left:54%;right:8%;top:43%;color:var(--ink)}
.p02__lead{font-size:2.3em;line-height:1;color:var(--navy)}
.p02__lead strong{display:block;font-size:1.15em}
.p02__right .body-copy{margin-top:.9em;font-size:.74em}
.p02 .folio{left:10%;color:var(--ink)}
.p02 .folio__url{color:#fff}

/* pages 03 / 04 */
.resort .photo{inset:0}
.resort__box{position:absolute;top:23%;height:52%;background:var(--navy);color:#fff;padding:3.4em 3em 0 3em}
.p03 .resort__box{left:46%;right:0}
.p04 .resort__box{left:0;right:45%}
.resort__box .heading{font-size:1.7em;margin-bottom:1em}
.resort__box .body-copy{font-size:.8em}
.resort .folio{color:#fff;border-color:rgba(255,255,255,.5)}
</style>
</head>
<body>

<div class="overview-sheet"></div>

<section class="spread spread--covers">
  <article class="page page--lg back">
    <div class="photo photo--faint" role="img" aria-label="Dimmed photo of a waiter serving guests in the hotel lobby"></div>
    <div class="back__brand brand">Azure Cove</div>
    <div class="back__contacts">
      <span class="contact"><svg viewBox="0 0 24 24"><path d="M6.6 10.8a15 15 0 006.6 6.6l2.2-2.2a1 1 0 011-.25 11.4 11.4 0 003.6.57 1 1 0 011 1V20a1 1 0 01-1 1A17 17 0 013 4a1 1 0 011-1h3.5a1 1 0 011 1 11.4 11.4 0 00.57 3.6 1 1 0 01-.25 1z"/></svg>123 456 7890</span>
      <span class="contact__sep">|</span>
      <span class="contact"><svg viewBox="0 0 24 24"><path d="M3 5h18v14H3zm2 2v.5l7 4.5 7-4.5V7l-7 4.5z"/></svg>info@website.com</span>
      <span class="contact__sep">|</span>
      <span class="contact"><svg viewBox="0 0 24 24"><path d="M12 2a10 10 0 100 20 10 10 0 000-20zm6.9 9h-3a15 15 0 00-1.3-5.6A8 8 0 0118.9 11zM12 4.1A13 13 0 0113.9 11h-3.8A13 13 0 0112 4.1zM9.4 5.4A15 15 0 008.1 11h-3a8 8 0 014.3-5.6zM5.1 13h3a15 15 0 001.3 5.6A8 8 0 015.1 13zM12 19.9A13 13 0 0110.1 13h3.8A13 13 0 0112 19.9zm2.6-1.3a15 15 0 001.3-5.6h3a8 8 0 01-4.3 5.6z"/></svg>www.website.com</span>
    </div>
  </article>
  <article class="page page--lg cover">
    <div class="cover__bar-left"></div>
    <div class="photo photo--pool" role="img" aria-label="Resort hotel with palm trees reflected in a swimming pool"></div>
    <div class="cover__brand brand">Azure Cove</div>
    <div class="cover__band"><h1 class="cover__title">HOSPITALITY<br>PROJECT</h1></div>
    <div class="cover__url">www.website.com</div>
    <div class="cover__bar-right"></div>
  </article>
</section>

<section class="spread spread--intro">
  <article class="page page--lg p01">
    <div class="photo photo--cafe" role="img" aria-label="Waitress serving two guests at a café table"></div>
    <h2 class="p01__title"><span class="p01__mark"></span>Lorem Ipsum</h2>
    <div class="p01__text">
      <p class="body-copy">Lorem Ipsum is simply dummy text of the printing and typesetting industry. Lorem Ipsum has been the industry's standard dummy text ever since the 1500s, when an unknown printer took a galley of type and scrambled it to make a type specimen book.</p>
      <p class="body-copy">Lorem Ipsum is simply dummy text of the printing and typesetting industry. Lorem Ipsum has been the industry's standard dummy text ever since the 1500s, when an unknown printer took a galley of type and scrambled it to make a type specimen book.</p>
    </div>
    <div class="folio"><span>www.website.com</span><span class="folio__no">01</span></div>
  </article>
  <article class="page page--lg p02">
    <div class="p02__panel"></div>
    <div class="photo photo--dining" role="img" aria-label="Restaurant interior with diners and pendant lights"></div>
    <div class="p02__left">
      <h3 class="heading">Lorem Ipsum</h3>
      <p class="body-copy">Lorem Ipsum is simply dummy text of the printing and typesetting industry. Lorem Ipsum has been the industry's standard dummy text ever since the 1500s, when an unknown printer took a galley of type and scrambled it to make a type specimen book.</p>
      <h3 class="heading">Lorem Ipsum</h3>
      <p class="body-copy">Lorem Ipsum is simply dummy text of the printing and typesetting industry. Lorem Ipsum has been the industry's standard dummy text ever since the 1500s, when an unknown printer took a galley of type and scrambled it to make a type specimen book.</p>
    </div>
    <div class="p02__right">
      <p class="p02__lead">Lorem<strong>Ipsum</strong></p>
      <p class="body-copy">Lorem Ipsum is simply dummy text of the printing and typesetting industry. Lorem Ipsum has been the industry's standard dummy text ever since the 1500s, when an unknown printer took a galley of type and scrambled it to make a type specimen book.</p>
      <p class="body-copy">Lorem Ipsum is simply dummy text of the printing and typesetting industry. Lorem Ipsum has been the industry's standard dummy text ever since the 1500s, when an unknown printer took a galley of type and scrambled it to make a type specimen book.</p>
    </div>
    <div class="folio"><span class="folio__url">www.website.com</span><span class="folio__no">02</span></div>
  </article>
</section>

<section class="spread spread--resort">
  <article class="page page--lg resort p03">
    <div class="photo photo--terrace" role="img" aria-label="Colourful resort buildings with red awnings beside a curved pool"></div>
    <div class="resort__box">
      <h3 class="heading">Lorem Ipsum</h3>
      <p class="body-copy">Lorem Ipsum is simply dummy text of the printing and typesetting industry. Lorem Ipsum has been the industry's standard dummy text ever since the 1500s, when an unknown printer took a galley of type and scrambled it to make a type specimen book.</p>
      <p class="body-copy">Lorem Ipsum is simply dummy text of the printing and typesetting industry. Lorem Ipsum has been the industry's standard dummy text ever since the 1500s, when an unknown printer took a galley of type and scrambled it to make a type specimen book.</p>
    </div>
    <div class="folio"><span>www.website.com</span><span class="folio__no">03</span></div>
  </article>
  <article class="page page--lg resort p04">
    <div class="photo photo--lagoon" role="img" aria-label="Long resort pool at sunset with lounge terraces"></div>
    <div class="resort__box">
      <h3 class="heading">Lorem Ipsum</h3>
      <p class="body-copy">Lorem Ipsum is simply dummy text of the printing and typesetting industry. Lorem Ipsum has been the industry's standard dummy text ever since the 1500s, when an unknown printer took a galley of type and scrambled it to make a type specimen book.</p>
      <p class="body-copy">Lorem Ipsum is simply dummy text of the printing and typesetting industry. Lorem Ipsum has been the industry's standard dummy text ever since the 1500s, when an unknown printer took a galley of type and scrambled it to make a type specimen book.</p>
    </div>
    <div class="folio"><span>www.website.com</span><span class="folio__no">04</span></div>
  </article>
</section>

<section class="grid">
  <article class="page page--sm cover">
    <div class="cover__bar-left"></div>
    <div class="photo photo--pool" role="img" aria-label="Resort hotel with palm trees reflected in a swimming pool"></div>
    <div class="cover__brand brand">Azure Cove</div>
    <div class="cover__band"><h2 class="cover__title">HOSPITALITY<br>PROJECT</h2></div>
    <div class="cover__url">www.website.com</div>
    <div class="cover__bar-right"></div>
  </article>
  <article class="page page--sm back">
    <div class="photo photo--faint" role="img" aria-label="Dimmed photo of a waiter serving guests in the hotel lobby"></div>
    <div class="back__brand brand">Azure Cove</div>
    <div class="back__contacts">
      <span class="contact"><svg viewBox="0 0 24 24"><path d="M6.6 10.8a15 15 0 006.6 6.6l2.2-2.2a1 1 0 011-.25 11.4 11.4 0 003.6.57 1 1 0 011 1V20a1 1 0 01-1 1A17 17 0 013 4a1 1 0 011-1h3.5a1 1 0 011 1 11.4 11.4 0 00.57 3.6 1 1 0 01-.25 1z"/></svg>123 456 7890</span>
      <span class="contact__sep">|</span>
      <span class="contact"><svg viewBox="0 0 24 24"><path d="M3 5h18v14H3zm2 2v.5l7 4.5 7-4.5V7l-7 4.5z"/></svg>info@website.com</span>
      <span class="contact__sep">|</span>
      <span class="contact"><svg viewBox="0 0 24 24"><path d="M12 2a10 10 0 100 20 10 10 0 000-20zm6.9 9h-3a15 15 0 00-1.3-5.6A8 8 0 0118.9 11zM12 4.1A13 13 0 0113.9 11h-3.8A13 13 0 0112 4.1zM9.4 5.4A15 15 0 008.1 11h-3a8 8 0 014.3-5.6zM5.1 13h3a15 15 0 001.3 5.6A8 8 0 015.1 13zM12 19.9A13 13 0 0110.1 13h3.8A13 13 0 0112 19.9zm2.6-1.3a15 15 0 001.3-5.6h3a8 8 0 01-4.3 5.6z"/></svg>www.website.com</span>
    </div>
  </article>
  <article class="page page--sm p01">
    <div class="photo photo--cafe" role="img" aria-label="Waitress serving two guests at a café table"></div>
    <h3 class="p01__title"><span class="p01__mark"></span>Lorem Ipsum</h3>
    <div class="p01__text">
      <p class="body-copy">Lorem Ipsum is simply dummy text of the printing and typesetting industry. Lorem Ipsum has been the industry's standard dummy text ever since the 1500s, when an unknown printer took a galley of type and scrambled it to make a type specimen book.</p>
      <p class="body-copy">Lorem Ipsum is simply dummy text of the printing and typesetting industry. Lorem Ipsum has been the industry's standard dummy text ever since the 1500s, when an unknown printer took a galley of type and scrambled it to make a type specimen book.</p>
    </div>
    <div class="folio"><span>www.website.com</span><span class="folio__no">01</span></div>
  </article>
  <article class="page page--sm p02">
    <div class="p02__panel"></div>
    <div class="photo photo--dining" role="img" aria-label="Restaurant interior with diners and pendant lights"></div>
    <div class="p02__left">
      <h3 class="heading">Lorem Ipsum</h3>
      <p class="body-copy">Lorem Ipsum is simply dummy text of the printing and typesetting industry. Lorem Ipsum has been the industry's standard dummy text ever since the 1500s, when an unknown printer took a galley of type and scrambled it to make a type specimen book.</p>
      <h3 class="heading">Lorem Ipsum</h3>
      <p class="body-copy">Lorem Ipsum is simply dummy text of the printing and typesetting industry. Lorem Ipsum has been the industry's standard dummy text ever since the 1500s, when an unknown printer took a galley of type and scrambled it to make a type specimen book.</p>
    </div>
    <div class="p02__right">
      <p class="p02__lead">Lorem<strong>Ipsum</strong></p>
      <p class="body-copy">Lorem Ipsum is simply dummy text of the printing and typesetting industry. Lorem Ipsum has been the industry's standard dummy text ever since the 1500s, when an unknown printer took a galley of type and scrambled it to make a type specimen book.</p>
      <p class="body-copy">Lorem Ipsum is simply dummy text of the printing and typesetting industry. Lorem Ipsum has been the industry's standard dummy text ever since the 1500s, when an unknown printer took a galley of type and scrambled it to make a type specimen book.</p>
    </div>
    <div class="folio"><span class="folio__url">www.website.com</span><span class="folio__no">02</span></div>
  </article>
  <article class="page page--sm resort p03">
    <div class="photo photo--terrace" role="img" aria-label="Colourful resort buildings with red awnings beside a curved pool"></div>
    <div class="resort__box">
      <h3 class="heading">Lorem Ipsum</h3>
      <p class="body-copy">Lorem Ipsum is simply dummy text of the printing and typesetting industry. Lorem Ipsum has been the industry's standard dummy text ever since the 1500s, when an unknown printer took a galley of type and scrambled it to make a type specimen book.</p>
      <p class="body-copy">Lorem Ipsum is simply dummy text of the printing and typesetting industry. Lorem Ipsum has been the industry's standard dummy text ever since the 1500s, when an unknown printer took a galley of type and scrambled it to make a type specimen book.</p>
    </div>
    <div class="folio"><span>www.website.com</span><span class="folio__no">03</span></div>
  </article>
  <article class="page page--sm resort p04">
    <div class="photo photo--lagoon" role="img" aria-label="Long resort pool at sunset with lounge terraces"></div>
    <div class="resort__box">
      <h3 class="heading">Lorem Ipsum</h3>
      <p class="body-copy">Lorem Ipsum is simply dummy text of the printing and typesetting industry. Lorem Ipsum has been the industry's standard dummy text ever since the 1500s, when an unknown printer took a galley of type and scrambled it to make a type specimen book.</p>
      <p class="body-copy">Lorem Ipsum is simply dummy text of the printing and typesetting industry. Lorem Ipsum has been the industry's standard dummy text ever since the 1500s, when an unknown printer took a galley of type and scrambled it to make a type specimen book.</p>
    </div>
    <div class="folio"><span>www.website.com</span><span class="folio__no">04</span></div>
  </article>
</section>

</body>
</html>
```